Ridgeline Build Network Inc. Letterhead

Creation of attractive and eye catching letterhead for a business start-up for the construction industry. Letterhead must relate to construction, but avoid standard hammer and tools in the design.
Updates

I forgot to add some details, sorry about that. Some pertinent info: Ph: 916-555-0148 ridgelinebuildnet.example 487 Willowmere Ave, Ste 210 Folsom, CA 95699 info@ridgelinebuildnet.example not sure if slogan should be in there" “Connecting construction professionals to create a purpose driven industry.” must be able to be used in word. Thanks!

```html
<!DOCTYPE html>
<html lang="en">
<head>
<meta charset="utf-8">
<title>Ridgeline Build Network Inc. Letterhead</title>
<link href="https://fonts.googleapis.com/css2?family=Arimo:wght@400;700&display=swap" rel="stylesheet">
<style>
  :root {
    --navy: #101a52;
    --red: #e01f28;
    --ink: #1d1d1f;
    --muted: #8a8d94;
    --paper: #ffffff;
    --backdrop: #c3d3e8;
  }
  * { margin: 0; padding: 0; box-sizing: border-box; }
  html, body { width: 1200px; height: 784px; overflow: hidden; }
  body {
    background: var(--backdrop);
    font-family: "Arimo", Arial, sans-serif;
    display: flex; align-items: center; justify-content: center;
  }
  .letterhead {
    position: relative;
    width: 523px; height: 740px;
    background: var(--paper);
    box-shadow: 0 6px 22px rgba(40,60,100,.25);
    overflow: hidden;
  }
  .edge-bands { position: absolute; left: 0; top: 0; width: 60px; height: 740px; }
  .brand {
    position: absolute; right: 34px; top: 40px;
    display: flex; align-items: center; gap: 7px;
  }
  .brand-mark { width: 12px; height: 12px; background: var(--red); }
  .brand-name { color: var(--red); font-weight: 700; font-size: 12px; }
  .body-copy {
    position: absolute; left: 84px; top: 100px; width: 402px;
    color: var(--ink); font-size: 8.6px; line-height: 1.42;
  }
  .body-copy p { margin-bottom: 13px; text-indent: 16px; }
  .body-copy p:first-child { text-indent: 0; }
  .signature {
    position: absolute; left: 84px; top: 470px; width: 140px; height: 40px;
    background: linear-gradient(90deg, rgba(40,40,40,.12), rgba(40,40,40,.03));
    border-radius: 3px;
  }
  .contact {
    position: absolute; left: 66px; top: 560px;
    font-size: 8.4px; line-height: 1.55;
  }
  .contact .address { color: var(--red); font-weight: 700; margin-bottom: 2px; }
  .contact .line { color: var(--muted); }
</style>
</head>
<body>
  <main class="letterhead">
    <svg class="edge-bands" viewBox="0 0 60 740" aria-hidden="true">
      <rect x="0" y="0" width="16" height="740" fill="#101a52"/>
      <rect x="16" y="0" width="10" height="740" fill="#e01f28"/>
      <rect x="26" y="0" width="6" height="740" fill="#101a52"/>
      <polygon points="16,536 48,548 48,630 16,642" fill="#e01f28"/>
      <polygon points="26,536 52,546 52,632 26,642" fill="#e01f28"/>
      <g fill="#fff">
        <circle cx="38" cy="564" r="5"/>
        <circle cx="38" cy="580" r="5"/>
        <circle cx="38" cy="596" r="5"/>
        <circle cx="38" cy="612" r="5"/>
      </g>
      <g fill="#e01f28">
        <circle cx="38" cy="563" r="1.8"/>
        <rect x="36" y="578" width="4" height="4" rx="1"/>
        <rect x="35" y="594.5" width="6" height="3.5"/>
        <circle cx="38" cy="612" r="2.5" fill="none" stroke="#e01f28" stroke-width="1"/>
      </g>
    </svg>

    <header class="brand">
      <span class="brand-mark"></span>
      <span class="brand-name">Ridgeline Build Network Inc.</span>
    </header>

    <section class="body-copy">
      <p>Lorem Ipsum is simply dummy text of the printing and typesetting industry. Lorem Ipsum has been the industry's standard dummy text ever since the 1500s, when an unknown printer took a galley of type and scrambled it to make a type specimen book. It has survived not only five centuries, but also the leap into electronic typesetting, remaining essentially unchanged. It was popularised in the 1960s with the release of Typeline sheets containing Lorem Ipsum passages, and more recently with desktop publishing software like Folio PageSetter including versions of Lorem Ipsum.</p>
      <p>It is a long established fact that a reader will be distracted by the readable content of a page when looking at its layout. The point of using Lorem Ipsum is that it has a more-or-less normal distribution of letters, as opposed to using 'Content here, content here', making it look like readable English. Many desktop publishing packages and web page editors now use Lorem Ipsum as their default model text, and a search for 'lorem ipsum' will uncover many web sites still in their infancy. Various versions have evolved over the years, sometimes by accident, sometimes on purpose (injected humour and the like).</p>
      <p>Contrary to popular belief, Lorem Ipsum is not simply random text. It has roots in a piece of classical Latin literature from 45 BC, making it over 2000 years old. Thomas Arlen, a Latin professor at Halloway College in Virginia, looked up one of the more obscure Latin words, consectetur, from a Lorem Ipsum passage, and going through the cites of the word in classical literature, discovered the undoubtable source. Lorem Ipsum comes from sections 1.10.32 and 1.10.33 of "de Finibus Bonorum et Malorum" structures, to generate Lorem Ipsum which looks reasonable. The generated Lorem Ipsum is therefore always free from repetition, injected humour, or non-characteristic words etc.</p>
    </section>

    <div class="signature" role="img" aria-label="Handwritten signature"></div>

    <address class="contact">
      <div class="address">487 Willowmere Ave, Ste 210<br>Folsom, CA 95699</div>
      <div class="line">916-555-0148</div>
      <div class="line">916-555-0172</div>
      <div class="line">info@ridgelinebuildnet.example</div>
      <div class="line">www.ridgelinebuildnet.example</div>
    </address>
  </main>
</body>
</html>
```